The Little Meadow Biscuit Bakery Swing Tag Label Design/Logo

Hi! We are looking for a “swing tag” label design for our different flavoured packs of (6) cookies. Basic info on the front (business name “The Little Meadow Biscuit Bakery”, strap line being “Handmade Gourmet Cookies” (not made in Norfolk) and the flavour “Choc Chip”, “Original”, “Choc Orange”, etc…).
The flavour part of the label being colour coded to suit, so dark brown for choc chip, beige for original, orange for choc orange, red/white for cranberry & white choc, bla bla bla!!
The rear of the tag to display ingredients, barcode, business postcode, suitable for Vegans, Dairy Free, Fenwick Approved Logo and Net Weight 300g.
Packaging is clear cellophane bags, with crimp seal. Three cookies stacked side by side with a brown Jute string tied around the packaging which will hold the tag.
We are selling in farm shops, deli’s and local food stores, so want to have a modern/smart feel to the design, yet retain the appeal of a small “cottage industry/countryside” style business.
The attached image is where we have got so far (with our very basic design skills) , but do not let this guide you too much, as we are looking for inspiration. (Appreciate the attached does not have the cottage/country appeal)!!
Size is undetermined, but thinking 100mm x 50mm, ish? Not ruled out a round label either, being cookies?
Labels will also be the basis for our business cards, internet pages (facebook, Instagram, etc…), so the design wants to be catchy, instantly recognisable and “say what it does on the tin”.
We also have single pack cookies in cellophane bags, so would be great if the deign could be printed in sticky label format also.
Not decided if the labels will be “craft paper” brown tags, or white, or another colour. Open to suggestions.
Like the idea of the “bite” out of the cookie, but needs “some teeth” if you get what I mean.
Feel free to message if you wish!
Thanks for your time.

Logo Text

The Little Meadow Biscuit Bakery or THE LITTLE MEADOW BISCUIT BAKERY

```html
<!DOCTYPE html>
<html lang="en">
<head>
<meta charset="UTF-8">
<title>The Little Meadow Biscuit Bakery – Flavour Tags</title>
<link rel="stylesheet" href="https://fonts.googleapis.com/css2?family=Nunito:wght@800;900&family=Yanone+Kaffeesatz:wght@300&display=swap">
<style>
  :root {
    --ink: #1d1d1b;
    --paper: #ffffff;
    --tag-edge: #c9c9c9;
    --original: #f6c48c;
    --stem-ginger: #b86c20;
    --choco-chip: #6b3418;
    --choco-orange: #e24a26;
    --white-choc: #1d1d1b;
    --mixed-spice: #583a93;
    --choco-mint: #72bd98;
    --choco-coconut: #57a9b5;
  }
  html, body {
    margin: 0;
    padding: 0;
    width: 1199px;
    height: 1200px;
    overflow: hidden;
    background: var(--paper);
  }
  .tag-sheet {
    position: relative;
    width: 1199px;
    height: 1200px;
  }
  .flavour-tag {
    position: absolute;
    width: 255px;
    height: 255px;
    border: 1px solid var(--tag-edge);
    background: var(--paper);
    box-sizing: content-box;
    overflow: hidden;
  }
  .brand-name {
    position: absolute;
    right: 12px;
    top: 16px;
    margin: 0;
    text-align: right;
    font-family: "Nunito", sans-serif;
    font-weight: 900;
    font-size: 26px;
    line-height: 30px;
    letter-spacing: 0.5px;
    color: var(--ink);
  }
  .brand-name span { display: block; }
  .flavour-disc {
    position: absolute;
    left: 13px;
    top: 125px;
    width: 82px;
    height: 82px;
    border-radius: 50%;
    display: flex;
    align-items: center;
    justify-content: center;
    text-align: center;
    font-family: "Nunito", sans-serif;
    font-weight: 800;
    font-size: 17px;
    line-height: 16px;
    color: var(--paper);
  }
  .strapline {
    position: absolute;
    left: 8px;
    right: 8px;
    bottom: 10px;
    margin: 0;
    font-family: "Yanone Kaffeesatz", sans-serif;
    font-weight: 300;
    font-size: 26px;
    line-height: 30px;
    text-align: center;
    color: var(--ink);
    white-space: nowrap;
  }
  .flavour-original { background: var(--original); color: var(--ink); }
  .flavour-stem-ginger { background: var(--stem-ginger); }
  .flavour-choco-chip { background: var(--choco-chip); }
  .flavour-choco-orange { background: var(--choco-orange); }
  .flavour-white-choc { background: var(--white-choc); }
  .flavour-mixed-spice { background: var(--mixed-spice); }
  .flavour-choco-mint { background: var(--choco-mint); }
  .flavour-choco-coconut { background: var(--choco-coconut); font-size: 15px; }
</style>
</head>
<body>
<main class="tag-sheet">

  <article class="flavour-tag" style="left:0;top:0;">
    <h1 class="brand-name"><span>THE LITTLE</span><span>MEADOW</span><span>BISCUIT</span><span>BAKERY</span></h1>
    <div class="flavour-disc flavour-original">original</div>
    <p class="strapline">Handmade Gourmet Cookies</p>
  </article>

  <article class="flavour-tag" style="left:471px;top:0;">
    <h1 class="brand-name"><span>THE LITTLE</span><span>MEADOW</span><span>BISCUIT</span><span>BAKERY</span></h1>
    <div class="flavour-disc flavour-stem-ginger">stem<br>ginger</div>
    <p class="strapline">Handmade Gourmet Cookies</p>
  </article>

  <article class="flavour-tag" style="left:942px;top:0;">
    <h1 class="brand-name"><span>THE LITTLE</span><span>MEADOW</span><span>BISCUIT</span><span>BAKERY</span></h1>
    <div class="flavour-disc flavour-choco-chip">choco<br>chip</div>
    <p class="strapline">Handmade Gourmet Cookies</p>
  </article>

  <article class="flavour-tag" style="left:0;top:471px;">
    <h1 class="brand-name"><span>THE LITTLE</span><span>MEADOW</span><span>BISCUIT</span><span>BAKERY</span></h1>
    <div class="flavour-disc flavour-choco-orange">choco<br>orange</div>
    <p class="strapline">Handmade Gourmet Cookies</p>
  </article>

  <article class="flavour-tag" style="left:471px;top:471px;">
    <h1 class="brand-name"><span>THE LITTLE</span><span>MEADOW</span><span>BISCUIT</span><span>BAKERY</span></h1>
    <div class="flavour-disc flavour-white-choc">white<br>choc</div>
    <p class="strapline">Handmade Gourmet Cookies</p>
  </article>

  <article class="flavour-tag" style="left:0;top:942px;">
    <h1 class="brand-name"><span>THE LITTLE</span><span>MEADOW</span><span>BISCUIT</span><span>BAKERY</span></h1>
    <div class="flavour-disc flavour-mixed-spice">mixed<br>spice</div>
    <p class="strapline">Handmade Gourmet Cookies</p>
  </article>

  <article class="flavour-tag" style="left:471px;top:942px;">
    <h1 class="brand-name"><span>THE LITTLE</span><span>MEADOW</span><span>BISCUIT</span><span>BAKERY</span></h1>
    <div class="flavour-disc flavour-choco-mint">choco<br>mint</div>
    <p class="strapline">Handmade Gourmet Cookies</p>
  </article>

  <article class="flavour-tag" style="left:942px;top:942px;">
    <h1 class="brand-name"><span>THE LITTLE</span><span>MEADOW</span><span>BISCUIT</span><span>BAKERY</span></h1>
    <div class="flavour-disc flavour-choco-coconut">choco<br>coconut</div>
    <p class="strapline">Handmade Gourmet Cookies</p>
  </article>

</main>
</body>
</html>
```